Medical Services Banner Set Project - revised

We need 3 standard size banner sets for each of two medical specialties: bariatric weight loss surgery and plastic surgery.
Our preference is for 3 versions of each set.
1. Interactive flash banner
2. Animated flash banner
3. Static banner
The theme is transition from ugly to beautiful and from fat to thin In looking at other similar banners we believe the key to proper execution is the rendering of the body transition.This is quite difficult to achieve - I have seen multiple attempts and no one can seem to get it just right (realistic and credible).
Action script for interactive banner begins with “before” image, click initiates the action script and image morphs into “after” image (beautiful/thin/sexy)
Animated is same but not interactive, transition on slow loop
Static version uses the” after” image only
Tags lines are respectively:
Stop Dieting and Start Living! (weight loss surgery)
Discover the New You! (plastic surgery)
Sizes:
300x250
728x90
160x600
Name of Company: Corvel Bariatric and Tamsen Cosmetic Surgery
Logo is attached - please do not use tag line

```html
<!DOCTYPE html>
<html lang="en">
<head>
<meta charset="utf-8">
<title>Vantorel Bariatric – Stop Dieting and Start Living</title>
<link rel="stylesheet" href="https://fonts.googleapis.com/css2?family=Marcellus&family=Arimo:ital,wght@1,700&display=swap">
<style>
  :root {
    --sky-deep: #2f8fd6;
    --sky-mid: #63b6ea;
    --sky-light: #bfe3f8;
    --paper: #ffffff;
    --brand-ink: #3b4a5c;
    --tag-outline: #1c5f9e;
    --skin-light: #f1cdb3;
    --skin-mid: #d9a17f;
    --skin-shadow: #b47c5e;
  }
  html, body {
    margin: 0;
    padding: 0;
    width: 1200px;
    height: 148px;
    overflow: hidden;
    background: var(--paper);
  }
  .banner {
    position: relative;
    width: 1200px;
    height: 148px;
    overflow: hidden;
    background: linear-gradient(90deg,
      var(--paper) 0px,
      var(--paper) 250px,
      var(--sky-light) 330px,
      var(--sky-mid) 560px,
      var(--sky-deep) 900px,
      var(--sky-mid) 1200px);
  }
  .banner__swoosh {
    position: absolute;
    inset: 0;
  }
  .photo {
    position: absolute;
    top: 0;
    height: 148px;
  }
  .photo--body {
    left: 792px;
    width: 208px;
    background: linear-gradient(180deg, var(--skin-mid) 0%, var(--skin-light) 55%, var(--skin-shadow) 100%);
  }
  .photo--face {
    left: 1000px;
    width: 200px;
    background: linear-gradient(90deg, var(--skin-shadow) 0%, var(--skin-light) 45%, var(--skin-mid) 100%);
  }
  .brand {
    position: absolute;
    left: 10px;
    top: 44px;
    display: flex;
    align-items: center;
    gap: 14px;
  }
  .brand__mark {
    width: 42px;
    height: 42px;
    border-radius: 50%;
    background: var(--brand-ink);
    flex: none;
  }
  .brand__name {
    font-family: "Marcellus", serif;
    color: var(--brand-ink);
    font-size: 34px;
    line-height: 36px;
    letter-spacing: 0.5px;
    text-transform: uppercase;
  }
  .tagline {
    position: absolute;
    margin: 0;
    font-family: "Arimo", sans-serif;
    font-style: italic;
    font-weight: 700;
    font-size: 30px;
    line-height: 1;
    color: var(--paper);
    text-transform: uppercase;
    white-space: nowrap;
    text-shadow:
      -1.5px -1.5px 0 var(--tag-outline),
      1.5px -1.5px 0 var(--tag-outline),
      -1.5px 1.5px 0 var(--tag-outline),
      1.5px 1.5px 0 var(--tag-outline),
      2px 3px 3px rgba(0, 40, 90, 0.45);
  }
  .tagline--primary { left: 314px; top: 62px; }
  .tagline--secondary { left: 504px; top: 108px; }
</style>
</head>
<body>
  <div class="banner">
    <svg class="banner__swoosh" width="1200" height="148" viewBox="0 0 1200 148" aria-hidden="true">
      <path d="M240 148 C420 60 640 30 1000 10" fill="none" stroke="#ffffff" stroke-opacity="0.45" stroke-width="18"/>
      <path d="M300 148 C520 90 720 70 1000 60" fill="none" stroke="#ffffff" stroke-opacity="0.3" stroke-width="10"/>
      <path d="M260 0 C420 40 620 44 980 24" fill="none" stroke="#ffffff" stroke-opacity="0.25" stroke-width="8"/>
    </svg>

    <div class="photo photo--body" role="img" aria-label="Photo of a slim waist with a measuring tape and a thumbs-up"></div>
    <div class="photo photo--face" role="img" aria-label="Photo of a woman's face marked for cosmetic surgery"></div>

    <div class="brand">
      <span class="brand__mark" aria-hidden="true"></span>
      <div class="brand__name">Vantorel<br>Bariatric</div>
    </div>

    <p class="tagline tagline--primary">Stop Dieting and Start Living!</p>
    <p class="tagline tagline--secondary">Discover the New You!</p>
  </div>
</body>
</html>
```